Artificial intelligence, machine learning, and automation company needs a sexy business card design

We need a sleek and sexy business card design for an AI consulting company based in Philadelphia PA. We provide custom machine learning and automation solutions for companies of all shapes and sizes. The primary industries that we serve are pharmaceuticals, engineering, healthcare, and computer software. We would like the designs to be a black business card that uses green as a sleek accent color. The final design should communicate intelligence, cutting edge new-tech, and optimization.

Target Market(s)

C-level and VP level executives of multi-million annual companies. Mostly in Pharma, Healthcare, Real Estate, Retail, and Engineering

Industry/Entity Type

Computer Software

Contact Information for Business Card

Name: Jack Moss
Title: CEO
Cell: 215 604 8293
Email: JackM@quillarcworks.example
Website: www.QuillarcWorks.example

Font styles to use
Sans Serif

Colors

Designer to choose colors to be used in the design.

Requirements
Must have
• 1) Attached Quillarc Logo (either with colors or not/embossed)
• 2) "Artificial Intelligence" "Automation" and "Machine Learning"
• 3) "Quillarc Laboratories" or "Quillarc Works" or "Quillarc"
• 4) Sexy AF.
Nice to have
• Black card / dark card color, "Quillarc Green" accent colors (in attached .ai file), Embossment of logo/name/etc, thick card stock, colored borders (on card sides, not front/back faces)
Should not have
• Should not be bland, or unsexy.

```html
<!DOCTYPE html>
<html lang="en">
<head>
<meta charset="UTF-8">
<title>Quillarc Laboratories – Business Card</title>
<link href="https://fonts.googleapis.com/css2?family=Montserrat:wght@400;500;700&display=swap" rel="stylesheet">
<style>
  :root {
    --stage: #1c1c1c;
    --card-top: #1b1b1b;
    --card-bottom: #0c0c0c;
    --gold: #c9a953;
    --gold-soft: #a98d45;
  }
  * { box-sizing: border-box; margin: 0; padding: 0; }
  html, body { width: 1200px; height: 900px; overflow: hidden; }
  body {
    background: var(--stage);
    font-family: 'Montserrat', sans-serif;
    color: var(--gold);
    display: flex;
    flex-direction: column;
    align-items: center;
    justify-content: center;
    gap: 36px;
  }
  .card {
    width: 700px;
    height: 400px;
    border-radius: 22px;
    background: linear-gradient(160deg, var(--card-top), var(--card-bottom));
    box-shadow: 0 10px 30px rgba(0,0,0,.55);
    position: relative;
  }
  /* Brand side */
  .card--brand {
    display: flex;
    flex-direction: column;
    align-items: center;
    justify-content: center;
  }
  .brand {
    display: flex;
    align-items: center;
    gap: 18px;
  }
  .brand__mark {
    width: 54px;
    height: 54px;
    border: 3px solid var(--gold);
  }
  .brand__name {
    font-weight: 500;
    text-transform: uppercase;
    line-height: 1.15;
    letter-spacing: 6px;
  }
  .brand--large .brand__name { font-size: 36px; }
  .brand__name span { display: block; font-size: .5em; letter-spacing: 7px; }
  .services {
    position: absolute;
    bottom: 42px;
    left: 0; right: 0;
    text-align: center;
    font-size: 16px;
    font-weight: 500;
    letter-spacing: 1px;
  }
  .services .sep { margin: 0 18px; }
  /* Contact side */
  .card--contact {
    display: grid;
    grid-template-columns: 300px 2px 1fr;
    align-items: center;
  }
  .card--contact .brand {
    flex-direction: column;
    gap: 14px;
    justify-self: center;
    text-align: center;
  }
  .card--contact .brand__mark { width: 80px; height: 80px; }
  .card--contact .brand__name { font-size: 26px; }
  .divider {
    width: 2px;
    height: 200px;
    background: var(--gold);
  }
  .contact { padding-left: 40px; }
  .contact__name {
    font-size: 26px;
    font-weight: 700;
    text-transform: uppercase;
    letter-spacing: 1px;
  }
  .contact__title {
    font-size: 14px;
    text-transform: uppercase;
    letter-spacing: 1px;
    margin: 4px 0 16px;
    color: var(--gold-soft);
  }
  .contact__line { font-size: 15px; font-weight: 500; line-height: 1.6; }
</style>
</head>
<body>
  <section class="card card--brand">
    <div class="brand brand--large">
      <div class="brand__mark"></div>
      <div class="brand__name">Quillarc<span>Laboratories</span></div>
    </div>
    <p class="services">Artificial Intelligence<span class="sep">/</span>Automation<span class="sep">/</span>Machine Learning</p>
  </section>

  <section class="card card--contact">
    <div class="brand">
      <div class="brand__mark"></div>
      <div class="brand__name">Quillarc<span>Laboratories</span></div>
    </div>
    <div class="divider"></div>
    <div class="contact">
      <h1 class="contact__name">Jack Moss</h1>
      <p class="contact__title">Chief Executive Officer</p>
      <p class="contact__line">2750 Linden Ave</p>
      <p class="contact__line">Philadelphia PA, 19130</p>
      <p class="contact__line">215 604 8293</p>
      <p class="contact__line">JackM@quillarcworks.example</p>
      <p class="contact__line">quillarcworks.example</p>
    </div>
  </section>
</body>
</html>
```